Looking for a contemporary business card design with our logo

would like to consider a embossing look although I'm not married to the idea. We are a custom jeweler that needs a look that represents old world craftsmanship with a modern twist that's why we went with a more modern shield type of logo that can be stamped inside our rings.
It could be two sided or one we are more after a look the pops and is trendy and creative. (WE ARE NOT LOOKING FOR A COOKIE CUTTER LAYOUT)
We have attached the image and will be using the logo with harwick studio wording in the format that it's in unless you see a better way of doing it.
If the logo needs a twist we are O.K. with suggestions as well.
This card should scream "Quality" from a high end studio.
Harwick Studio
4186 Maplecrest Rd. Unit B-2
Larkfield, OR 80317
www.harwickstudio-example.com
lu@harwickstudio-example.com
Should speak quality craftsmanship

```html
<!DOCTYPE html>
<html lang="en">
<head>
<meta charset="utf-8">
<title>Harwick Studio – Business Card</title>
<link rel="stylesheet" href="https://fonts.googleapis.com/css2?family=Lato:wght@400;700;900&display=swap">
<style>
  :root {
    --backdrop: #e4e4e4;
    --paper: #ffffff;
    --ink: #111111;
    --ink-soft: #2b2b2b;
    --card-dark: #262628;
    --card-dark-edge: #1e1e20;
    --deboss: #3c3c3f;
    --band-text: #f2f2f2;
  }
  * { box-sizing: border-box; margin: 0; padding: 0; }
  html, body {
    width: 1200px; height: 720px; overflow: hidden;
    background: var(--backdrop);
    font-family: "Lato", Arial, sans-serif;
  }
  .stage { position: relative; width: 1200px; height: 720px; }

  .card {
    position: absolute; top: 241px;
    width: 420px; height: 239px; overflow: hidden;
  }
  .card--front { left: 147px; background: var(--paper); }
  .card--back {
    left: 633px;
    background: linear-gradient(135deg, var(--card-dark) 0%, var(--card-dark-edge) 100%);
  }

  /* front */
  .brand {
    position: absolute; left: 20px; top: 36px;
    display: flex; align-items: center; gap: 8px;
  }
  .brand__mark { width: 22px; height: 22px; background: var(--ink); }
  .brand__name {
    font-weight: 700; font-size: 19px; letter-spacing: 0.5px;
    color: var(--ink); text-transform: uppercase;
  }

  .contact {
    position: absolute; left: 20px; top: 152px;
    list-style: none; font-size: 11px; color: var(--ink-soft);
  }
  .contact__item { display: flex; align-items: center; gap: 6px; height: 13.5px; }
  .contact__icon { width: 10px; height: 10px; fill: var(--ink); }

  .person {
    position: absolute; right: 21px; top: 150px; text-align: right;
  }
  .person__name { font-weight: 900; font-size: 15px; color: var(--ink); letter-spacing: 0.2px; }
  .person__role { font-size: 10px; color: var(--ink-soft); margin-top: 2px; }

  .rule {
    position: absolute; left: 0; right: 0; top: 216px;
    height: 2px; background: var(--ink);
  }
  .address-band {
    position: absolute; left: 0; right: 0; top: 220px; bottom: 0;
    background: var(--ink); color: var(--band-text);
    font-size: 11px; text-align: center; line-height: 19px;
    white-space: nowrap;
  }

  /* back */
  .back-brand {
    position: absolute; left: 0; right: 0; top: 92px;
    display: flex; align-items: center; justify-content: center; gap: 12px;
  }
  .back-brand__mark { width: 30px; height: 30px; border: 2px solid var(--deboss); }
  .back-brand__name {
    font-weight: 700; font-size: 26px; letter-spacing: 1px;
    color: var(--deboss); text-transform: uppercase;
  }
  .back-web {
    position: absolute; left: 0; right: 0; top: 214px;
    text-align: center; font-size: 10px; color: var(--deboss);
  }
</style>
</head>
<body>
<main class="stage">
  <section class="card card--front" aria-label="Card front">
    <div class="brand">
      <span class="brand__mark"></span>
      <span class="brand__name">Harwick Studio</span>
    </div>

    <ul class="contact">
      <li class="contact__item">
        <svg class="contact__icon" viewBox="0 0 10 10" aria-hidden="true">
          <path d="M1 2.5C1 1.5 2 1 5 1s4 .5 4 1.5V4H7V3H3v1H1z M2.5 5h5l1 4h-7z"/>
        </svg>
        <span>541-555-0148</span>
      </li>
      <li class="contact__item">
        <svg class="contact__icon" viewBox="0 0 10 10" aria-hidden="true">
          <path d="M0.5 2h9v6h-9z M1.2 2.6 5 5.4 8.8 2.6" fill="none" stroke="#111" stroke-width="1"/>
        </svg>
        <span>lu@harwickstudio-example.com</span>
      </li>
      <li class="contact__item">
        <svg class="contact__icon" viewBox="0 0 10 10" aria-hidden="true">
          <g fill="none" stroke="#111" stroke-width="0.9">
            <circle cx="5" cy="5" r="4.3"/>
            <ellipse cx="5" cy="5" rx="1.8" ry="4.3"/>
            <path d="M0.7 5h8.6 M1.5 2.8h7 M1.5 7.2h7"/>
          </g>
        </svg>
        <span>www.harwickstudio-example.com</span>
      </li>
    </ul>

    <div class="person">
      <p class="person__name">Dale Morrow</p>
      <p class="person__role">President</p>
    </div>

    <div class="rule"></div>
    <p class="address-band">4186 Maplecrest Road Unit B-2, Larkfield, OR 80317</p>
  </section>

  <section class="card card--back" aria-label="Card back">
    <div class="back-brand">
      <span class="back-brand__mark"></span>
      <span class="back-brand__name">Harwick Studio</span>
    </div>
    <p class="back-web">www.harwickstudio-example.com</p>
  </section>
</main>
</body>
</html>
```